Verdanix Medical Business Card

Create a high class Business card for Medical Aesthetics and Wellness Practice called Verdanix Medical Aesthetics and Wellness as per the logo attached.
Addresss is: 418 Harlan Brook Road Suite 312 Melville, New York 11093
Phone (555)204-7391 IG @verdanix_medical
Verdanixmedical.example

I need 5 different name configurations
1) Dr. Theo Valcourt
Aesthetics and Wellness Specialist
Medical Director

2) Rosalind Pettinger, NP
Clinical Nurse Manager

3) Marla Vostrik, RN
Aesthetic Nurse Specialist

4) Petra Halvesen, RN

5) Dana Kowbeck, L.E.
Senior Licensed Esthetician

Target Market(s)

22-55 Females

Industry/Entity Type

Medical Spa and Wellness

Contact Information for Business Card

Logo, address, phone, web, instagram, providers name

Requirements
Must have
• Attractive classy modern look

```html
<!DOCTYPE html>
<html lang="en">
<head>
<meta charset="utf-8">
<title>Verdanix Medical Business Card</title>
<link rel="stylesheet" href="https://fonts.googleapis.com/css2?family=Cormorant+Garamond:wght@400&family=Lato:wght@400;700;900&display=swap">
<style>
  :root {
    --teal: #134f62;
    --teal-dark: #0f4354;
    --white: #ffffff;
    --ink: #3f4a4f;
    --rule: #d5dadc;
    --backdrop: #2a2c30;
  }
  html, body {
    margin: 0;
    width: 1200px;
    height: 952px;
    overflow: hidden;
    background: var(--backdrop);
  }
  .canvas {
    position: relative;
    width: 1200px;
    height: 952px;
  }
  .card {
    position: absolute;
    width: 640px;
    height: 366px;
    box-shadow: 0 14px 40px rgba(0,0,0,.45);
    overflow: hidden;
  }
  .card-front {
    left: 120px;
    top: 70px;
    background: var(--teal);
    color: var(--white);
    display: flex;
    flex-direction: column;
    align-items: center;
    justify-content: center;
  }
  .card-back {
    left: 440px;
    top: 516px;
    background: var(--white);
  }
  .brand-name {
    font-family: "Cormorant Garamond", serif;
    font-weight: 400;
    font-size: 78px;
    letter-spacing: 2px;
    line-height: 1;
    margin: 0;
  }
  .brand-tagline {
    font-family: "Cormorant Garamond", serif;
    font-size: 19px;
    letter-spacing: 1.5px;
    text-transform: uppercase;
    margin: 14px 0 0;
  }
  .brand-city {
    font-family: "Cormorant Garamond", serif;
    font-size: 13px;
    letter-spacing: 9px;
    text-transform: uppercase;
    margin: 10px 0 0;
  }
  .accent-bar {
    position: absolute;
    background: var(--teal);
  }
  .accent-top { left: 0; top: 40px; width: 26px; height: 70px; }
  .accent-bottom { right: 0; bottom: 30px; width: 150px; height: 60px; }
  .back-brand {
    position: absolute;
    left: 60px;
    top: 92px;
    width: 230px;
    color: var(--teal);
    text-align: center;
  }
  .back-brand .brand-name { font-size: 44px; letter-spacing: 1px; }
  .back-brand .brand-tagline { font-size: 10.5px; margin-top: 8px; letter-spacing: 1px; }
  .back-brand .brand-city { font-size: 8px; letter-spacing: 6px; margin-top: 6px; }
  .divider {
    position: absolute;
    left: 320px;
    top: 70px;
    width: 1px;
    height: 150px;
    background: var(--rule);
  }
  .contact {
    position: absolute;
    left: 348px;
    top: 84px;
    font-family: "Lato", sans-serif;
    color: var(--ink);
  }
  .person-name {
    font-weight: 900;
    font-size: 19px;
    letter-spacing: .5px;
    color: var(--teal);
    text-transform: uppercase;
    margin: 0;
  }
  .person-name .credential { font-size: 12px; }
  .person-role {
    font-size: 15px;
    margin: 3px 0 16px;
  }
  .contact-list { list-style: none; padding: 0; margin: 0; }
  .contact-list li {
    display: flex;
    align-items: center;
    gap: 8px;
    font-size: 14px;
    line-height: 22px;
  }
  .contact-list svg { width: 13px; height: 13px; fill: var(--teal); flex: none; }
  .address {
    position: absolute;
    left: 60px;
    top: 268px;
    font-family: "Lato", sans-serif;
    font-size: 14px;
    color: var(--ink);
    margin: 0;
  }
</style>
</head>
<body>
<main class="canvas">
  <section class="card card-front">
    <p class="brand-name">Verdanix</p>
    <p class="brand-tagline">Medical Aesthetics and Wellness</p>
    <p class="brand-city">New York</p>
  </section>

  <section class="card card-back">
    <div class="accent-bar accent-top"></div>
    <div class="accent-bar accent-bottom"></div>

    <div class="back-brand">
      <p class="brand-name">Verdanix</p>
      <p class="brand-tagline">Medical Aesthetics and Wellness</p>
      <p class="brand-city">New York</p>
    </div>

    <div class="divider"></div>

    <div class="contact">
      <p class="person-name">Rosalind Pettinger<span class="credential">, NP</span></p>
      <p class="person-role">Clinical Nurse Manager</p>
      <ul class="contact-list">
        <li>
          <svg viewBox="0 0 16 16" aria-hidden="true"><path d="M3.5 1l2.5 3-1.5 1.8c.9 2 2.5 3.6 4.6 4.6L11 8.9l3 2.5-1.3 2.8C7 13.8 2.2 9 1.8 3.2z"/></svg>
          (555)204-7391 IG
        </li>
        <li>
          <svg viewBox="0 0 16 16" aria-hidden="true"><path d="M1 3h14v10H1z M1.5 3.5L8 9l6.5-5.5" stroke="#fff" stroke-width="1"/></svg>
          @verdanix_medical
        </li>
        <li>
          <svg viewBox="0 0 16 16" aria-hidden="true"><circle cx="8" cy="8" r="7"/><path d="M1 8h14M8 1c-3 3.5-3 10.5 0 14M8 1c3 3.5 3 10.5 0 14" stroke="#fff" stroke-width="1" fill="none"/></svg>
          Verdanixmedical.example
        </li>
      </ul>
    </div>

    <p class="address">418 Harlan Brook Road Suite 312 Melville, New York 11093</p>
  </section>
</main>
</body>
</html>
```